Business Card Design Project

New Business Card design for Varodine Technology Ltd using new Logo and new Tagline for staffing company.

About us from our website - www.varodine.example:

VaroDine is a leading and recognized Electronic Entertainment, Workforce Augmentation, and Project Management solutions provider with clients in Electronic Entertainment, Legal, Technology, Government and other verticals that range in size from start up organizations to Zenlar 500 companies. VaroDine is certified as an 8(a) minority and woman owned enterprise, established in 1998.

Target Market(s)

Companies in Electronic Entertainment, Legal, Government and Technology

Industry/Entity Type

Business

Requirements
Must have
• Must include in small letters the following information on back:

Established in 1998
8(a)(w)(e), Cage #7KRT9, DUNS #462137580

Front should have the following:
Derek Holloway
Vice President
5820 Birchmont Road
Fallowby, FB 482917
555-318-2746 X 100
555-902-6613 Fax
555-318-2746 Toll Free
name@varodine.example

Our Tagline: Connect • Collaborate • Achieve

```html
<!DOCTYPE html>
<html lang="en">
<head>
<meta charset="utf-8">
<title>VaroDine Business Card</title>
<link rel="stylesheet" href="https://fonts.googleapis.com/css2?family=Questrial&display=swap">
<style>
  :root {
    --ink: #1c1c1c;
    --band: #2a2829;
    --brand-blue: #0a8fce;
    --paper: #ffffff;
    --mist: #eef4f8;
    --tagline-grey: #a6a6a6;
    --tagline-shadow: #7d7d7d;
    --light-text: #ffffff;
    --soft-text: #bdbdbd;
  }
  * { margin: 0; padding: 0; box-sizing: border-box; }
  html, body {
    width: 1200px;
    height: 900px;
    overflow: hidden;
    background: var(--paper);
  }
  .card {
    position: relative;
    width: 1200px;
    height: 900px;
    font-family: "Questrial", Arial, sans-serif;
    background: var(--paper);
    overflow: hidden;
  }
  .top-rule {
    position: absolute;
    left: 0; top: 59px;
    width: 100%; height: 3px;
    background: var(--ink);
  }
  .front-field {
    position: absolute;
    left: 0; top: 62px;
    width: 100%; height: 535px;
    background: radial-gradient(ellipse 70% 60% at 45% 45%, var(--mist) 0%, rgba(238,244,248,0.4) 60%, rgba(255,255,255,0) 100%);
  }
  .address {
    position: absolute;
    right: 18px; top: 66px;
    width: 424px;
    font-size: 27px;
    line-height: 35px;
    letter-spacing: 0.6px;
    color: var(--ink);
    font-style: normal;
    white-space: nowrap;
  }
  .wordmark {
    position: absolute;
    left: 85px; top: 240px;
    width: 1000px;
    display: flex;
    align-items: center;
    justify-content: center;
    gap: 28px;
  }
  .wordmark-dot {
    width: 46px; height: 46px;
    border-radius: 50%;
    background: var(--brand-blue);
    flex: none;
  }
  .wordmark-name {
    font-size: 118px;
    line-height: 1;
    letter-spacing: 10px;
    color: var(--brand-blue);
  }
  .contact-band {
    position: absolute;
    left: 0; top: 597px;
    width: 100%; height: 231px;
    background: var(--band);
  }
  .contact-list {
    position: absolute;
    left: 45px; top: 48px;
    list-style: none;
    font-size: 27px;
    line-height: 36.5px;
    letter-spacing: 0.5px;
    color: var(--light-text);
  }
  .person {
    position: absolute;
    right: 45px; top: 50px;
    text-align: right;
    color: var(--light-text);
  }
  .person-name {
    font-size: 32px;
    line-height: 40px;
    letter-spacing: 0.5px;
  }
  .person-title {
    font-size: 24px;
    line-height: 34px;
    color: var(--soft-text);
  }
  .credentials {
    position: absolute;
    right: 45px; bottom: 22px;
    text-align: right;
    font-size: 15px;
    line-height: 21px;
    color: var(--soft-text);
  }
  .bottom-rule {
    position: absolute;
    left: 0; top: 833px;
    width: 100%; height: 12px;
    background: var(--band);
  }
  .tagline {
    position: absolute;
    right: 17px; top: 848px;
    font-size: 30px;
    color: var(--tagline-grey);
    letter-spacing: 0;
    text-shadow: 1px 1px 0 var(--tagline-shadow);
    white-space: nowrap;
  }
</style>
</head>
<body>
  <main class="card">
    <div class="top-rule"></div>
    <div class="front-field"></div>

    <address class="address">
      5820 Birchmont Road, Suite 340<br>
      Fallowby, FB 482917
    </address>

    <div class="wordmark">
      <span class="wordmark-dot"></span>
      <span class="wordmark-name">VARODINE</span>
    </div>

    <section class="contact-band">
      <ul class="contact-list">
        <li>555-318-2746 X 100</li>
        <li>555-902-6613 Fax</li>
        <li>555-318-2746 Toll Free</li>
        <li>name@varodine.example</li>
      </ul>
      <div class="person">
        <p class="person-name">Derek Holloway</p>
        <p class="person-title">Vice President</p>
      </div>
      <div class="credentials">
        <p>Established in 1998</p>
        <p>8(a)(w)(e), Cage #7KRT9, DUNS #462137580</p>
      </div>
    </section>

    <div class="bottom-rule"></div>
    <p class="tagline">Our Tagline: Connect • Collaborate • Achieve</p>
  </main>
</body>
</html>
```